Brookvane Estates LLC stationary for a real estate property management company.

Create stationary (letterhead, envelopes, business cards) using Brookvane Estates LLC logo as primary creative element. Stationary design needs to be horizontal, leaving as much space as possible for correspondence copy. See attached Creative Brief and past stationary files for details.

Target Market(s)

Prospective apartment residents and current residents, vendors, and government agencies.

Industry/Entity Type

Property Management

Contact Information for Business Card

Business card employee title: Property Manager. Should include address, phone, fax, email, website, slogan, and Brookvane Estates logo.

Font styles to use
Sans Serif

Colors
0592cd
000000

Requirements
Must have
• Tone should be conservative, institutional, business (i.e. banking, finance, real estate). Must include: address, phone, fax, website, and slogan (see attached Creative Brief). Should be a horizontal design, leaving as much room as possible for letter correspondence copy.
Nice to have
• Please use an Arial or Helvetica style font.
Should not have
• Letterhead layout should leave as much room as possible for copy.

```html
<!DOCTYPE html>
<html lang="en">
<head>
<meta charset="utf-8">
<title>Brookvane Estates LLC — Stationery</title>
<link href="https://fonts.googleapis.com/css2?family=Lato:wght@400;700&display=swap" rel="stylesheet">
<style>
  :root {
    --board: #c5bfad;
    --paper: #ffffff;
    --blue: #1565a8;
    --ink: #1e1e1e;
    --charcoal: #3d3d3f;
    --mist: #e9eaec;
    --pale-blue: #e6eef6;
    --shadow: 2px 3px 4px rgba(60, 55, 40, 0.35);
  }
  * { box-sizing: border-box; margin: 0; padding: 0; }
  html, body { width: 1200px; height: 1200px; overflow: hidden; }
  body { background: var(--board); font-family: "Lato", Arial, sans-serif; color: var(--ink); position: relative; }

  .sheet { position: absolute; background: var(--paper); box-shadow: var(--shadow); overflow: hidden; }
  .card { width: 318px; height: 182px; top: 179px; }
  .card--front { left: 70px; }
  .card--back { left: 443px; }
  .card--pattern { left: 817px; }
  .letterhead { left: 70px; top: 434px; width: 482px; height: 623px; }
  .envelope { left: 602px; width: 550px; height: 246px; }
  .envelope--front { top: 466px; }
  .envelope--back { top: 758px; }

  .lockup { position: absolute; display: flex; align-items: center; gap: 5px; white-space: nowrap; }
  .lockup__dot { border-radius: 50%; background: var(--blue); flex: none; }
  .lockup__name { color: var(--blue); font-weight: 700; letter-spacing: 0.01em; }
  .lockup__name--stacked { line-height: 1.05; }

  .person__name { font-size: 13px; }
  .person__title { font-size: 9px; margin-top: 2px; }

  .contacts { position: absolute; font-size: 10px; line-height: 12.5px; }
  .contacts li { list-style: none; display: flex; align-items: center; gap: 5px; white-space: nowrap; }
  .contacts .gap { margin-top: 5px; }
  .icon { width: 10px; height: 10px; flex: none; }
  .address { color: var(--blue); font-size: 10.5px; line-height: 12px; margin-top: 6px; }

  /* front card */
  .card--front .person { position: absolute; left: 24px; top: 23px; }
  .card--front .person__name { color: var(--blue); }
  .card--front .contacts { left: 24px; top: 82px; }
  .card--front .accent { position: absolute; right: -34px; bottom: -54px; width: 150px; height: 150px; border-radius: 50%; background: var(--blue); }

  /* back card */
  .card--back .lockup { left: 21px; top: 96px; }
  .card--back .person { position: absolute; left: 162px; top: 30px; }
  .card--back .person__title { color: var(--charcoal); font-size: 9.5px; }
  .card--back .contacts { left: 162px; top: 78px; font-size: 9.5px; line-height: 12px; }
  .card--back .contacts .address { font-size: 10px; line-height: 11.5px; margin-top: 3px; }

  /* pattern card */
  .pattern-field { position: absolute; inset: 0; background: linear-gradient(180deg, #f2f2f3, #ebebec); }
  .card--pattern .lockup { right: 20px; bottom: 17px; background: var(--paper); padding: 4px 6px; }

  /* letterhead */
  .letterhead .lockup { left: 50px; top: 36px; }
  .letterhead .watermark { position: absolute; left: 288px; top: 293px; width: 300px; height: 300px; border-radius: 50%; background: var(--pale-blue); }
  .letterhead .footer-rule { position: absolute; left: 51px; right: 51px; top: 595px; height: 2px; background: var(--blue); }
  .letterhead .footer { position: absolute; left: 56px; top: 601px; display: flex; gap: 7px; font-size: 6.4px; white-space: nowrap; }
  .letterhead .footer span { display: flex; align-items: center; gap: 3px; }
  .letterhead .footer .icon { width: 7px; height: 7px; }

  /* envelopes */
  .envelope--front .lockup { left: 20px; top: 24px; }
  .return-address { position: absolute; left: 150px; top: 23px; padding-left: 7px; border-left: 1px solid var(--blue); font-size: 7px; line-height: 8.5px; color: var(--charcoal); }
  .flap { position: absolute; left: 0; top: 0; width: 550px; height: 86px; }
  .envelope--back .seal { position: absolute; left: 255px; top: 17px; width: 40px; height: 40px; border-radius: 50%; background: var(--blue); }
</style>
</head>
<body>

<svg width="0" height="0" style="position:absolute">
  <defs>
    <symbol id="i-phone" viewBox="0 0 10 10"><rect x="0.5" y="1.5" width="9" height="7.5" rx="1" fill="#1565a8"/><rect x="2" y="4" width="6" height="3.5" fill="#fff"/><rect x="1.5" y="0.5" width="7" height="2" rx="1" fill="#1565a8"/></symbol>
    <symbol id="i-fax" viewBox="0 0 10 10"><rect x="0.5" y="3" width="9" height="6.5" rx="1" fill="#1565a8"/><rect x="2.5" y="0.5" width="5" height="3.5" fill="#1565a8"/><rect x="2.5" y="5.5" width="5" height="2.5" fill="#fff"/></symbol>
    <symbol id="i-mail" viewBox="0 0 10 10"><rect x="0.5" y="1.5" width="9" height="7" rx="1" fill="#1565a8"/><rect x="1.7" y="3" width="6.6" height="4.2" fill="#fff"/></symbol>
    <symbol id="i-web" viewBox="0 0 10 10"><circle cx="5" cy="5" r="4.3" fill="none" stroke="#1565a8" stroke-width="1.1"/><ellipse cx="5" cy="5" rx="1.8" ry="4.3" fill="none" stroke="#1565a8" stroke-width="0.9"/><line x1="0.7" y1="5" x2="9.3" y2="5" stroke="#1565a8" stroke-width="0.9"/></symbol>
    <symbol id="i-pin" viewBox="0 0 10 10"><rect x="0.5" y="0.5" width="9" height="9" rx="1" fill="#1565a8"/><circle cx="5" cy="4.2" r="2" fill="#fff"/><path d="M3.4 5.3 L5 8.3 L6.6 5.3Z" fill="#fff"/></symbol>
  </defs>
</svg>

<!-- Business card front -->
<section class="sheet card card--front">
  <div class="person">
    <p class="person__name">Dana Whitfield</p>
    <p class="person__title">Property manager</p>
  </div>
  <ul class="contacts">
    <li><svg class="icon"><use href="#i-phone"/></svg>555-310-4820</li>
    <li><svg class="icon"><use href="#i-fax"/></svg>555-310-4865</li>
    <li class="gap"><svg class="icon"><use href="#i-mail"/></svg>dana@brookvaneestates.com</li>
    <li><svg class="icon"><use href="#i-web"/></svg>www.brookvaneestates.com</li>
    <li class="address">2750 Harbor View Dr. #120<br>Fairhaven, CA 92140</li>
  </ul>
  <div class="accent"></div>
</section>

<!-- Business card back -->
<section class="sheet card card--back">
  <div class="lockup">
    <span class="lockup__dot" style="width:22px;height:22px"></span>
    <span class="lockup__name lockup__name--stacked" style="font-size:12px">BROOKVANE<br>ESTATES LLC</span>
  </div>
  <div class="person">
    <p class="person__name">Dana Whitfield</p>
    <p class="person__title">Property manager</p>
  </div>
  <ul class="contacts">
    <li><svg class="icon"><use href="#i-phone"/></svg>555-310-4820</li>
    <li><svg class="icon"><use href="#i-fax"/></svg>555-310-4865</li>
    <li class="gap"><svg class="icon"><use href="#i-mail"/></svg>dana@brookvaneestates.com</li>
    <li><svg class="icon"><use href="#i-web"/></svg>www.brookvaneestates.com</li>
    <li class="address">2750 Harbor View Dr. #120<br>Fairhaven, CA 92140</li>
  </ul>
</section>

<!-- Business card pattern side -->
<section class="sheet card card--pattern">
  <div class="pattern-field" role="img" aria-label="Faint repeating brand pattern in light grey"></div>
  <div class="lockup">
    <span class="lockup__dot" style="width:20px;height:20px"></span>
    <span class="lockup__name" style="font-size:12.5px">BROOKVANE ESTATES LLC</span>
  </div>
</section>

<!-- Letterhead -->
<section class="sheet letterhead">
  <div class="lockup">
    <span class="lockup__dot" style="width:20px;height:20px"></span>
    <span class="lockup__name" style="font-size:12.5px">BROOKVANE ESTATES LLC</span>
  </div>
  <div class="watermark"></div>
  <div class="footer-rule"></div>
  <div class="footer">
    <span><svg class="icon"><use href="#i-phone"/></svg>555-310-4820</span>
    <span><svg class="icon"><use href="#i-fax"/></svg>555-310-4865</span>
    <span><svg class="icon"><use href="#i-pin"/></svg>2750 Harbor View Dr. #120&nbsp;&nbsp;Fairhaven, CA 92140</span>
    <span><svg class="icon"><use href="#i-web"/></svg>www.brookvaneestates.com</span>
  </div>
</section>

<!-- Envelope front -->
<section class="sheet envelope envelope--front">
  <div class="lockup">
    <span class="lockup__dot" style="width:14px;height:14px"></span>
    <span class="lockup__name" style="font-size:8.5px">BROOKVANE ESTATES LLC</span>
  </div>
  <p class="return-address">2750 Harbor View Dr. #120<br>Fairhaven, CA 92140</p>
</section>

<!-- Envelope back -->
<section class="sheet envelope envelope--back">
  <svg class="flap" viewBox="0 0 550 86" aria-hidden="true">
    <path d="M1 0 L8 80 Q9 84 14 84 L538 84 Q543 84 544 80 L549 0" fill="#fff" stroke="#d8d8d8" stroke-width="1"/>
    <line x1="10" y1="86" x2="542" y2="86" stroke="#e2e2e2" stroke-width="2"/>
  </svg>
  <div class="seal"></div>
</section>

</body>
</html>
```